書籍の表紙デザインをしていただける方をコンペにて募集いたします。 現在認知症予防になる生活習慣を書籍を制作しております。 こちらにある書籍のような、マンガと解説を組み合わせた構成になる予定です。 https://www.torimaru-shoten.jp/bk/4/2860/7/ 制作いただきたいのは表紙デザイン1点となります。 こちらも上記ページにあるもののように、イラスト+文字の表紙にしていただきたく思います。 帯の部分もアリの形でお願いします。 サイズはA5を予定しております。 メインターゲットは60代くらいの女性となります。 使用していただきたいイラストは添付しております。 以下が文言となります。 ↓ マンガでわかる 医学博士がすすめる 朝の散歩で若返る毎日の工夫 ← タイトル 初期認知症患者の9割が改善!? 世界で話題の予防・治療法が わかる! 実践できる! 執筆: 堀内達郎 作画: 菅野 渉 一般社団法人はつらつ会議 ←ロゴ ・契約金額 : 3万円(税込) ご質問等あればお気軽にお送りください。 ご応募お待ちしております。 |
もっともバランスがよく、目を引くデザインだと感じましたので採用させていただきました。
たくさんの素敵なご提案ありがとうございました。ひとつに絞らなければならないのが大変心苦しく感じました。また機会がありましたらよろしくお願いいたします。

```html
<!DOCTYPE html>
<html lang="ja">
<head>
<meta charset="utf-8">
<title>朝の散歩で若返る毎日の工夫</title>
<link rel="stylesheet" href="https://fonts.googleapis.com/css2?family=Noto+Sans+JP:wght@500;700;900&family=M+PLUS+Rounded+1c:wght@800&display=swap">
<style>
  :root {
    --green: #5aaa2c;
    --green-dark: #3f8a1c;
    --ink: #2b2b2b;
    --paper: #ffffff;
    --line: #cfcfcf;
    --illus-top: #f3e6da;
    --illus-bottom: #d9c6b4;
  }
  html, body { margin: 0; padding: 0; overflow: hidden; background: var(--paper); }
  .cover {
    position: relative;
    width: 848px; height: 1200px;
    overflow: hidden;
    background: var(--paper);
    box-sizing: border-box;
    border: 2px solid var(--line);
    font-family: "Noto Sans JP", sans-serif;
    color: var(--ink);
  }
  .illustration {
    position: absolute;
    left: 30px; top: 150px;
    width: 470px; height: 680px;
    border-radius: 220px 220px 0 0;
    background: linear-gradient(180deg, var(--illus-top), var(--illus-bottom));
  }
  .badge {
    position: absolute;
    left: 150px; top: 18px;
    width: 170px; height: 170px;
    border-radius: 50%;
    background: var(--green);
    color: var(--paper);
    display: flex; flex-direction: column; align-items: center; justify-content: center;
    font-family: "M PLUS Rounded 1c", sans-serif;
    font-weight: 800;
    font-size: 38px; line-height: 1.15;
    transform: rotate(-12deg);
  }
  .endorsement {
    position: absolute;
    right: 40px; top: 62px;
    margin: 0;
    font-weight: 900; font-size: 50px; letter-spacing: 1px;
  }
  .title {
    position: absolute;
    right: 36px; top: 160px;
    margin: 0;
    text-align: right;
    font-weight: 900;
    line-height: 1.1;
  }
  .title span { display: block; }
  .title .line-a, .title .line-c { font-size: 88px; color: var(--ink); }
  .title .line-b { font-size: 128px; color: var(--green); }
  .credits {
    position: absolute;
    left: 512px; top: 700px;
    margin: 0;
    font-weight: 700; font-size: 34px; line-height: 1.6;
  }
  .obi {
    position: absolute;
    left: 0; right: 0; top: 830px; height: 290px;
    background: var(--green);
  }
  .obi-lead {
    position: absolute;
    left: 26px; right: 26px; top: 28px; height: 96px;
    background: var(--paper);
    border-radius: 14px;
    display: flex; align-items: center; justify-content: center;
    font-weight: 900; font-size: 48px;
  }
  .obi-lead .num {
    display: inline-flex; align-items: center; justify-content: center;
    width: 70px; height: 70px; margin: 0 6px;
    border-radius: 50%;
    background: var(--green); color: var(--paper);
    font-size: 52px;
  }
  .obi-copy {
    position: absolute;
    left: 0; right: 0; top: 140px;
    margin: 0;
    text-align: center;
    color: var(--paper);
    font-weight: 900; font-size: 54px; line-height: 1.3;
  }
  .publisher {
    position: absolute;
    left: 0; right: 0; top: 1120px; height: 80px;
    display: flex; align-items: center; justify-content: center; gap: 16px;
    background: var(--paper);
  }
  .publisher-mark { width: 50px; height: 50px; border-radius: 50%; background: var(--green); }
  .publisher-name { display: flex; flex-direction: column; line-height: 1.1; }
  .publisher-name small { font-size: 14px; font-weight: 500; }
  .publisher-name strong { font-size: 30px; font-weight: 700; }
</style>
</head>
<body>
<div class="cover">
  <div class="illustration" role="img" aria-label="イラスト：笑顔の年配女性の肩に手を置く若い女性"></div>

  <div class="badge"><span>マンガで</span><span>わかる</span></div>
  <p class="endorsement">医学博士が認める</p>

  <h1 class="title">
    <span class="line-a">朝の散歩で</span>
    <span class="line-b">若返る</span>
    <span class="line-c">毎日の工夫</span>
  </h1>

  <p class="credits">執筆：堀内達郎<br>作画：菅野 渉</p>

  <section class="obi">
    <div class="obi-lead">初期認知症患者の<span class="num">9</span>割が改善!?</div>
    <p class="obi-copy">世界で話題の予防・治療法が<br>わかる！実践できる！</p>
  </section>

  <footer class="publisher">
    <span class="publisher-mark"></span>
    <span class="publisher-name">
      <small>Hatsuratsu Kaigi Association</small>
      <strong>一般社団法人はつらつ会議</strong>
    </span>
  </footer>
</div>
</body>
</html>
```